Marlow Fern Publishing
Dale P. Hartwick
Author-Publisher-Speaker
5127 Birchmoor Court Idaho Falls, ID 83499
DaleHartwick@marlowfernpress.com
http://marlowfernpress.com
o Fiction and non-fiction books o Writing o Editing o Layout design o Marketing/promotion o Photography o Publication start-ups/management
The back of the business card should contain the 4/color photo, company name, logo and the line "Books that Reach the Higher Ground."

```html
<!DOCTYPE html>
<html lang="en">
<head>
<meta charset="utf-8">
<title>Marlow Fern Publishing — Stationery</title>
<link href="https://fonts.googleapis.com/css2?family=Cinzel:wght@600&family=Open+Sans:wght@400;600&display=swap" rel="stylesheet">
<style>
  :root {
    --brand-red: #9c1b22;
    --brand-red-dark: #7a1218;
    --paper: #ffffff;
    --paper-shade: #f1f1f1;
    --swoosh-grey: #c9c9c9;
    --ink: #4a4a4a;
    --backdrop: #e8e4de;
  }
  * { box-sizing: border-box; margin: 0; padding: 0; }
  html, body { width: 1200px; height: 655px; overflow: hidden; }
  body { background: var(--backdrop); font-family: "Open Sans", sans-serif; color: var(--ink); position: relative; }

  .piece { position: absolute; background: var(--paper); box-shadow: 0 2px 6px rgba(0,0,0,.18); overflow: hidden; }
  .piece svg.wave { position: absolute; left: 0; bottom: 0; width: 100%; }

  .wordmark { font-family: "Cinzel", serif; font-weight: 600; color: var(--brand-red); letter-spacing: .02em; white-space: nowrap; }
  .tagline { font-family: "Cinzel", serif; font-weight: 600; color: var(--brand-red); letter-spacing: .06em; white-space: nowrap; }
  .on-red .wordmark, .on-red .tagline { color: var(--paper); }

  .fine { font-size: 5.5px; line-height: 1.45; color: var(--ink); white-space: nowrap; }

  /* Business cards */
  .card { left: 72px; width: 264px; height: 160px; border-radius: 10px; }
  .card-front { top: 100px; }
  .card-front .wordmark { position: absolute; left: 22px; top: 46px; font-size: 11px; }
  .card-front .person { position: absolute; left: 22px; top: 70px; }
  .card-front .person-name { font-size: 6.5px; font-weight: 600; color: var(--brand-red); }
  .card-front .contact { position: absolute; right: 18px; top: 72px; text-align: right; }
  .card-plain { top: 288px; }
  .card-plain .brand, .card-back .brand { position: absolute; left: 0; right: 0; top: 64px; text-align: center; }
  .card-plain .wordmark, .card-back .wordmark { font-size: 14px; }
  .card-plain .tagline, .card-back .tagline { font-size: 5px; margin-top: 4px; }
  .card-back { top: 468px; background: var(--brand-red); }

  /* Letterhead */
  .letterhead-under { left: 392px; top: 108px; width: 326px; height: 460px; transform: rotate(-2deg); background: var(--paper-shade); }
  .letterhead { left: 372px; top: 96px; width: 326px; height: 458px; }
  .letterhead .brand { position: absolute; left: 42px; top: 46px; }
  .letterhead .wordmark { font-size: 11px; }
  .letterhead .tagline { font-size: 4px; margin-top: 2px; }
  .letterhead .footer { position: absolute; right: 26px; bottom: 12px; text-align: right; color: #fff; font-size: 5px; line-height: 1.5; }

  /* Envelopes */
  .envelope-back-red { left: 756px; top: 221px; width: 372px; height: 140px; }
  .envelope-back-red .brand { position: absolute; left: 0; right: 0; top: 30px; text-align: center; }
  .envelope-back-red .wordmark { font-size: 9px; }
  .envelope-back-white { left: 701px; top: 329px; width: 355px; height: 150px; }
  .envelope-front { left: 749px; top: 427px; width: 374px; height: 132px; }
  .envelope-front .brand { position: absolute; left: 26px; top: 22px; }
  .envelope-front .wordmark { font-size: 11px; }
  .envelope-front .tagline { font-size: 4px; margin-top: 2px; }
  .envelope-front .return { position: absolute; right: 18px; bottom: 8px; text-align: right; color: #fff; font-size: 5px; line-height: 1.5; }
  svg.flap { position: absolute; left: 0; top: 0; width: 100%; height: 100%; }
</style>
</head>
<body>

<section class="piece card card-front">
  <div class="wordmark">Marlow Fern Publishing</div>
  <div class="person">
    <div class="person-name">Dale P. Hartwick</div>
    <div class="fine">Author-Publisher-Speaker</div>
  </div>
  <div class="contact fine">
    <div>5127 Birchmoor Court</div>
    <div>Idaho Falls, ID 83499</div>
    <div>DaleHartwick@marlowfernpress.com</div>
    <div>http://marlowfernpress.com</div>
  </div>
  <svg class="wave" viewBox="0 0 264 50" height="50" preserveAspectRatio="none">
    <path d="M0 22 C70 48 170 10 264 28 L264 50 L0 50Z" fill="var(--swoosh-grey)"/>
    <path d="M0 32 C80 52 170 22 264 36 L264 50 L0 50Z" fill="var(--brand-red)"/>
  </svg>
</section>

<section class="piece card card-plain">
  <div class="brand">
    <div class="wordmark">Marlow Fern Publishing</div>
    <div class="tagline">Books that Reach the Higher Ground</div>
  </div>
</section>

<section class="piece card card-back on-red">
  <div class="brand">
    <div class="wordmark">Marlow Fern Publishing</div>
    <div class="tagline">Books that Reach the Higher Ground</div>
  </div>
</section>

<div class="piece letterhead-under"></div>
<section class="piece letterhead">
  <div class="brand">
    <div class="wordmark">Marlow Fern Publishing</div>
    <div class="tagline">Books that Reach the Higher Ground</div>
  </div>
  <svg class="wave" viewBox="0 0 326 70" height="70" preserveAspectRatio="none">
    <path d="M0 18 C90 46 200 0 326 20 L326 70 L0 70Z" fill="var(--swoosh-grey)"/>
    <path d="M0 28 C100 54 210 10 326 28 L326 70 L0 70Z" fill="var(--brand-red)"/>
  </svg>
  <div class="footer">
    <div>5127 Birchmoor Court Idaho Falls, ID 83499</div>
    <div>DaleHartwick@marlowfernpress.com</div>
    <div>http://marlowfernpress.com</div>
  </div>
</section>

<section class="piece envelope-back-red on-red">
  <svg class="flap" viewBox="0 0 372 140" preserveAspectRatio="none">
    <path d="M0 0 L372 0 L372 40 C300 70 230 92 186 96 C140 92 70 70 0 40Z" fill="var(--brand-red)"/>
    <path d="M0 140 L150 80 M372 140 L222 80" stroke="#e2e2e2" stroke-width="1" fill="none"/>
  </svg>
  <div class="brand"><div class="wordmark">Marlow Fern Publishing</div></div>
</section>

<section class="piece envelope-back-white">
  <svg class="flap" viewBox="0 0 355 150" preserveAspectRatio="none">
    <path d="M0 0 L178 92 L355 0" stroke="#d6d6d6" stroke-width="1.2" fill="none"/>
    <path d="M0 150 L140 80 M355 150 L215 80" stroke="#e4e4e4" stroke-width="1" fill="none"/>
  </svg>
</section>

<section class="piece envelope-front">
  <div class="brand">
    <div class="wordmark">Marlow Fern Publishing</div>
    <div class="tagline">Books that Reach the Higher Ground</div>
  </div>
  <svg class="wave" viewBox="0 0 374 56" height="56" preserveAspectRatio="none">
    <path d="M0 14 C110 44 240 0 374 18 L374 56 L0 56Z" fill="var(--swoosh-grey)"/>
    <path d="M0 24 C120 52 250 10 374 26 L374 56 L0 56Z" fill="var(--brand-red)"/>
  </svg>
  <div class="return">
    <div>5127 Birchmoor Court Idaho Falls, ID 83499</div>
    <div>http://marlowfernpress.com</div>
  </div>
</section>

</body>
</html>
```